Xmas Greeting for Email for Corvath Solutions

We would love to have a beautifully designed Xmas card that we can send to our clients .
The card will be used to thank our clients for their support during the year and to wish them a Merry Xmas and a Good New year (2020).

We would like a design that is simple and very elegant.

Target Market(s)

Our clients

Font styles to use
Script

Colors

Designer to choose colors to be used in the design.

Requirements
Must have
• 1. Our logo (see attached)
• 2. A message that thanks our clients for their support during the year.
• 3. the message "Merry Christmas & Happy New Year"
• 4. Design must be simple and elegant

```html
<!DOCTYPE html>
<html lang="en">
<head>
<meta charset="utf-8">
<title>Corvath Solutions – Season's Greetings</title>
<link rel="stylesheet" href="https://fonts.googleapis.com/css2?family=Cinzel:wght@400;500&family=Kaushan+Script&family=Yellowtail&display=swap">
<style>
  :root {
    --stage: #ececef;
    --navy: #14244a;
    --navy-deep: #0e1a38;
    --gold: #c9a227;
    --berry: #b01230;
    --berry-dark: #7e0a20;
    --ink: #111316;
    --white: #ffffff;
    --sky-top: #2f7fb8;
    --sky-mid: #6fa6cc;
    --snow: #d9dee4;
  }
  * { margin: 0; padding: 0; box-sizing: border-box; }
  html, body {
    width: 1200px; height: 1200px; overflow: hidden;
    background: var(--stage);
  }
  .card {
    position: absolute; left: 143px; top: 29px;
    width: 914px; height: 1141px; overflow: hidden;
  }
  .card-backdrop {
    position: absolute; inset: 0;
    background:
      radial-gradient(ellipse 420px 520px at 10% 35%, #2a86b8 0%, rgba(42,134,184,0) 70%),
      linear-gradient(180deg, var(--sky-top) 0%, #3f8cc2 35%, var(--sky-mid) 60%, #c5d3de 78%, var(--snow) 100%);
  }
  .gold-frame {
    position: absolute; left: 19px; top: 21px; width: 877px; height: 1100px;
    border: 3px solid var(--gold);
  }
  .greeting-band {
    position: absolute; left: 0; top: 88px; width: 914px; height: 142px;
    background: linear-gradient(180deg, var(--navy) 0%, var(--navy-deep) 100%);
    border-top: 4px solid var(--gold);
    border-bottom: 4px solid var(--gold);
    color: var(--white); text-align: center;
  }
  .salutation {
    position: absolute; left: 0; right: 0; top: 18px;
    font-family: "Yellowtail", cursive; font-size: 40px; line-height: 1;
  }
  .wish-lead {
    position: absolute; left: 0; right: 0; top: 78px;
    font-family: "Cinzel", serif; font-size: 31px; letter-spacing: 0.5px; line-height: 1;
  }
  .headline {
    position: absolute; font-family: "Kaushan Script", cursive;
    color: var(--berry); line-height: 1; white-space: nowrap;
    text-shadow: 0 0 0 var(--white), 3px 3px 0 var(--white), -3px -3px 0 var(--white),
                 3px -3px 0 var(--white), -3px 3px 0 var(--white), 0 6px 10px rgba(126,10,32,0.35);
  }
  .headline-merry { left: 245px; top: 345px; font-size: 132px; }
  .headline-christmas { left: 195px; top: 478px; font-size: 132px; }
  .new-year-lead {
    position: absolute; left: 410px; top: 637px;
    font-family: "Cinzel", serif; font-size: 30px; color: var(--ink); line-height: 1;
  }
  .new-year {
    position: absolute; left: 404px; top: 672px;
    font-family: "Cinzel", serif; font-size: 58px; color: var(--ink); line-height: 1;
  }
  .thanks {
    position: absolute; left: 0; right: 0; top: 852px; text-align: center;
    font-family: "Cinzel", serif; font-size: 26px; color: var(--ink); line-height: 1;
  }
  .brand {
    position: absolute; left: 0; right: 0; top: 970px;
    display: flex; align-items: center; justify-content: center; gap: 22px;
  }
  .brand-dot {
    width: 86px; height: 86px; border-radius: 50%; background: var(--navy);
  }
  .brand-name {
    font-family: "Cinzel", serif; font-size: 34px; letter-spacing: 4px;
    color: var(--berry); line-height: 1;
  }
</style>
</head>
<body>
  <main class="card">
    <div class="card-backdrop" role="img" aria-label="Frosted blue pine branches with hanging glass baubles, red glitter snowflakes and soft snowy bokeh"></div>
    <div class="gold-frame"></div>

    <header class="greeting-band">
      <p class="salutation">Dear esteemed client,</p>
      <p class="wish-lead">CORVATH SOLUTIONS WISHES YOU A</p>
    </header>

    <h1>
      <span class="headline headline-merry">Merry</span>
      <span class="headline headline-christmas">Christmas</span>
    </h1>
    <p class="new-year-lead">AND A PROSPEROUS</p>
    <p class="new-year">NEW YEAR</p>

    <p class="thanks">Thank you for your continued loyalty &amp; support</p>

    <footer class="brand">
      <span class="brand-dot"></span>
      <span class="brand-name">CORVATH SOLUTIONS</span>
    </footer>
  </main>
</body>
</html>
```